ultra-minimalist business card

front (black background, matte):

tarik b. hosseny
writer | photographer
get@tarikhosseny.com

back (white background, matte):

a picture speaks a thousand words;
a word draws a thousand pictures.

www.tarikhosseny.com

all text should be small (white or silver - as long as it shows against the black - on the front; black or gray - as long as it shows against the white - on the back).

feel free to get creative in terms of arrangement, alignment, and font type, but remember, the overall style is minimalist, so nothing too fancy, please.

thanks.

```html
<!DOCTYPE html>
<html lang="en">
<head>
<meta charset="utf-8">
<title>Tarik B. Hosseny — Business Card</title>
<link rel="stylesheet" href="https://fonts.googleapis.com/css2?family=PT+Sans+Narrow:wght@400;700&display=swap">
<style>
  :root {
    --page: #ffffff;
    --card-front: #000000;
    --card-back: #ffffff;
    --ink-light: #ffffff;
    --ink-dark: #1a1a1a;
    --rule: #cfcfcf;
  }
  * { margin: 0; padding: 0; box-sizing: border-box; }
  html, body {
    width: 848px;
    height: 1200px;
    overflow: hidden;
    background: var(--page);
  }
  .sheet {
    position: relative;
    width: 848px;
    height: 1200px;
    font-family: "PT Sans Narrow", "Arial Narrow", sans-serif;
  }
  .card {
    position: absolute;
    left: 124px;
    width: 601px;
    height: 344px;
  }
  .card--front {
    top: 221px;
    background: var(--card-front);
    color: var(--ink-light);
  }
  .card--back {
    top: 636px;
    background: var(--card-back);
    border: 1px solid var(--rule);
    color: var(--ink-dark);
  }
  .identity {
    position: absolute;
    top: 121px;
    left: 0;
    right: 0;
    text-align: center;
    font-size: 18px;
    line-height: 34.5px;
    letter-spacing: 2.6px;
  }
  .motto {
    position: absolute;
    top: 112px;
    left: 0;
    right: 0;
    text-align: center;
    font-size: 16px;
    line-height: 27px;
    letter-spacing: 0.4px;
  }
  .quote-mark {
    position: absolute;
    top: 96px;
    font-weight: 700;
    font-size: 38px;
    line-height: 1;
  }
  .quote-mark--open { left: 137px; }
  .quote-mark--close { left: 386px; }
  .website {
    position: absolute;
    bottom: 16px;
    left: 0;
    right: 0;
    text-align: center;
    font-size: 16px;
    letter-spacing: 1.2px;
  }
</style>
</head>
<body>
  <main class="sheet">
    <section class="card card--front" aria-label="Card front">
      <div class="identity">
        <p class="identity__name">tarik b. hosseny</p>
        <p class="identity__role">writer | photographer</p>
        <p class="identity__email">get@tarikhosseny.com</p>
      </div>
    </section>

    <section class="card card--back" aria-label="Card back">
      <span class="quote-mark quote-mark--open" aria-hidden="true">&ldquo;</span>
      <blockquote class="motto">
        <p>a picture speaks a thousand words;</p>
        <p>a word draws a thousand pictures.</p>
      </blockquote>
      <span class="quote-mark quote-mark--close" aria-hidden="true">&rdquo;</span>
      <p class="website">www.tarikhosseny.com</p>
    </section>
  </main>
</body>
</html>
```